An organizational wellness program flyer - The CLIMB Program flyer

Need a 2 page PDF and/or tri-fold marketing piece for a program that will be marketed to mid-large employer groups (100-5000 employees). The program is designed to reduce healthcare costs by providing knowledge, tools and techniques to increase employee self-awareness and self-agency. The program details are provided in the uploaded files.
Use the phrase "How much is chronic stress and burnout costing your organization?" as a headline
The designs should highlight the ROI through reduced healthcare costs, employee turnover and absenteeism and increased employee health and engagement.
The description of the CLIMB acronym should be included and prominent The "Cultivating Lasting Insight, Motivation and Balance".
Include The CLIMB Program framework
Do not include the details of the pathways. Only include the Pathway heading/title.
Have also provided scripts from marketing videos to inform what's included on the flyer, but do not include the scripts on the brochure.
Looking for something clean, not too text heavy but includes the right data points.
Include the phrase "This is not just a program. It's a paradigm shift." at the
Would like all of the source data files so that I can modify later if needed.
Include the BrindaVale logo on the brochure. www.brindavale.com for brand colors.
organizations with 100-5000 employees; organizations looking for wellness programs
- Clean, compelling visuals
- Images of me on the brochure

```html
<!DOCTYPE html>
<html lang="en">
<head>
<meta charset="utf-8">
<title>The CLIMB Program – BrindaVale Brochure</title>
<link rel="stylesheet" href="https://fonts.googleapis.com/css2?family=Zilla+Slab:wght@600;700&family=Poppins:wght@400;500;600;700&display=swap">
<style>
:root{
  --bg:#e4e4e4;
  --white:#ffffff;
  --leaf:#7ab32e;
  --forest:#5f9a2b;
  --deep:#2e5a12;
  --lime:#eefb8c;
  --lime-soft:#f5fdb8;
  --tile:#8fc33a;
  --bark:#4a3524;
  --ink:#333333;
  --photo-a:#9a9a9a;
  --photo-b:#4a4a4a;
  --slab:"Zilla Slab", Georgia, serif;
  --sans:"Poppins", Arial, sans-serif;
}
*{margin:0;padding:0;box-sizing:border-box}
html,body{width:1200px;height:871px;overflow:hidden}
body{background:var(--bg);position:relative;font-family:var(--sans)}
.spread{position:absolute;top:210px;width:856px;height:662px;background:var(--white);transform:scale(.68);transform-origin:0 0;overflow:hidden;box-shadow:0 6px 18px rgba(0,0,0,.25)}
.spread--outside{left:12px}
.spread--inside{left:606px}
.abs{position:absolute}
.photo{position:absolute;background:linear-gradient(160deg,var(--photo-a),var(--photo-b))}
.slab{font-family:var(--slab);font-weight:700}

/* outside */
.intro-head{left:35px;top:32px;font-size:22px;line-height:1.12;color:var(--deep)}
.panel-green-left{left:53px;top:148px;width:240px;height:514px;background:var(--leaf);border-top-left-radius:42px}
.intro-copy{left:83px;top:181px;width:170px;font-size:11px;line-height:1.45;color:#1f3a0a}
.panel-lime{left:285px;top:98px;width:285px;height:564px;background:var(--lime);border-radius:52px 52px 0 0}
.cta-head{left:310px;top:168px;font-size:32px;line-height:1.08;color:var(--deep)}
.contact{left:310px;color:var(--deep);display:flex;align-items:center;gap:8px}
.contact--phone{top:554px;font-size:21px;font-weight:500}
.contact--web{top:586px;font-size:16px;font-weight:600}
.brand{display:flex;flex-direction:column;align-items:center;gap:4px;color:var(--bark);font-family:var(--slab);font-weight:600}
.brand__dot{width:38px;height:38px;border-radius:50%;background:var(--leaf)}
.brand--cover{left:590px;top:20px;width:220px;font-size:22px}
.tag{left:585px;background:var(--bark);color:var(--white);font-size:11px;padding:4px 6px}
.tag--1{top:116px}
.tag--2{top:142px}
.panel-green-right{left:570px;top:146px;width:235px;height:516px;background:var(--forest);border-top-right-radius:42px}
.discover{left:587px;top:196px;color:var(--white);width:210px;z-index:2}
.discover__lead{font-size:17px;font-weight:600}
.discover__title{font-size:36px;line-height:1;margin:4px 0 4px}
.discover__sub{font-size:17px;font-weight:600;line-height:1.2}
.discover__note{margin-top:18px;font-size:12.5px;line-height:1.4}

/* inside */
.field{left:53px;top:0;width:750px;height:510px;background:var(--forest);border-bottom-right-radius:42px}
.about{left:58px;top:18px;color:var(--white);font-size:14px;font-weight:600}
.acronym{left:20px;top:38px;list-style:none}
.acronym li{display:flex;align-items:center;height:39px;color:var(--white);font-family:var(--slab);font-weight:700;font-size:29px}
.acronym .cap{width:40px;height:33px;background:var(--lime);color:var(--deep);border-radius:16px;display:flex;align-items:center;justify-content:center;margin-right:4px}
.acronym small{font-family:var(--sans);font-size:15px;font-weight:600;margin-left:8px;align-self:flex-end;margin-bottom:6px}
.about-copy{left:64px;top:232px;width:200px;font-size:9.5px;line-height:1.35;color:var(--white)}
.about-copy p+p{margin-top:7px}
.benefit{left:68px;display:flex;align-items:center;gap:10px;color:var(--lime);font-size:10.5px;line-height:1.2;width:205px}
.benefit__icon{width:40px;height:32px;border-radius:16px;background:var(--lime);display:flex;align-items:center;justify-content:center;flex:none}
.benefit--1{top:356px}
.benefit--2{top:396px}
.framework-title{left:333px;top:16px;color:var(--white);font-size:17px}
.framework-title b{font-family:var(--slab);font-size:20px}
.steps{left:250px;top:48px}
.step-label{position:absolute;font-size:8.5px;line-height:1.25;color:var(--white);width:95px}
.panel-goal{left:285px;top:218px;width:285px;height:444px;background:var(--lime);border-radius:52px 52px 0 0;text-align:center}
.goal-lead{position:absolute;left:30px;top:22px;width:225px;font-size:10.5px;font-weight:600;line-height:1.35;color:var(--deep)}
.goal-head{position:absolute;left:10px;top:72px;width:265px;font-size:21px;line-height:1.1;color:var(--deep)}
.tree-title{position:absolute;left:0;top:140px;width:285px;font-size:13.5px;font-weight:500;color:var(--deep)}
.tree{position:absolute;left:0;top:160px}
.pillar{position:absolute;top:194px;width:80px;height:42px;background:var(--forest);color:var(--white);font-size:9.5px;line-height:1.15;display:flex;align-items:center;justify-content:center;text-align:center;border:1px solid var(--deep)}
.tile{position:absolute;width:80px;height:31px;background:var(--tile);color:var(--white);font-size:7.5px;line-height:1.15;display:flex;align-items:center;justify-content:center;text-align:center;border:1px solid var(--lime-soft)}
.c1{left:10px}.c2{left:102px}.c3{left:193px}
.r1{top:272px}.r2{top:322px}.r3{top:372px}
.invest{left:585px;top:228px;color:var(--white)}
.invest__lead{font-size:10.5px;font-weight:600;line-height:1.35}
.invest__head{font-size:21px;line-height:1.1;margin-top:2px}
.stat{left:588px;display:flex;align-items:center;gap:14px;color:var(--white)}
.stat__num{font-family:var(--sans);font-size:31px;font-weight:500;color:transparent;-webkit-text-stroke:1.2px var(--lime);width:72px}
.stat__text{font-size:9.5px;font-weight:600;line-height:1.3;width:120px}
.stat--1{top:325px}.stat--2{top:386px}.stat--3{top:448px}
.roi{left:585px;top:540px;color:var(--ink);font-size:12px;line-height:1.45}
.roi__value{font-size:20px;color:var(--forest);line-height:1.1}
.brand--back{left:705px;top:560px;width:130px;font-size:17px}
.brand--back .brand__dot{width:30px;height:30px}
</style>
</head>
<body>

<section class="spread spread--outside" aria-label="Brochure outside">
  <h2 class="abs intro-head slab">This isn’t just another<br>wellness program..<br>It’s a science-backed,<br>proven framework.</h2>
  <div class="abs panel-green-left"></div>
  <p class="abs intro-copy">It empowers employees to take control of their well-being, creating a healthier and more productive workforce.</p>
  <div class="photo" style="left:90px;top:292px;width:195px;height:370px;border-radius:90px 90px 0 0" role="img" aria-label="Black and white portrait of a smiling woman in a blazer"></div>

  <div class="abs panel-lime"></div>
  <h2 class="abs cta-head slab">Ready to<br>redefine<br>wellness<br>in your<br>organization?</h2>
  <p class="abs contact contact--phone">
    <svg width="14" height="14" viewBox="0 0 14 14" aria-hidden="true"><rect x="1" y="2" width="12" height="10" rx="2" fill="none" stroke="#2e5a12" stroke-width="1.5"/><line x1="5" y1="2" x2="5" y2="12" stroke="#2e5a12" stroke-width="1.5"/></svg>
    555 010 2040</p>
  <p class="abs contact contact--web">
    <svg width="14" height="14" viewBox="0 0 14 14" aria-hidden="true"><circle cx="7" cy="7" r="6" fill="none" stroke="#2e5a12" stroke-width="1.3"/><ellipse cx="7" cy="7" rx="2.6" ry="6" fill="none" stroke="#2e5a12" stroke-width="1.1"/><line x1="1" y1="7" x2="13" y2="7" stroke="#2e5a12" stroke-width="1.1"/></svg>
    www.brindavale.com</p>

  <div class="abs brand brand--cover"><span class="brand__dot"></span>BrindaVale</div>
  <p class="abs tag tag--1">How much is chronic stress &amp; burnout</p>
  <div class="abs panel-green-right"></div>
  <p class="abs tag tag--2">costing your organization?</p>
  <div class="photo" style="left:700px;top:420px;width:156px;height:242px;border-radius:70px 0 0 0" role="img" aria-label="Black and white photo of a laughing woman pointing upward"></div>
  <div class="abs discover">
    <p class="discover__lead">Discover how the</p>
    <p class="discover__title slab">CLIMB<br>Program</p>
    <p class="discover__sub">can transform your workplace</p>
    <p class="discover__note">CLIMB Program is<br>not just a Program.<br>It’s a Paradigm Shift.</p>
  </div>
</section>

<section class="spread spread--inside" aria-label="Brochure inside">
  <div class="abs field"></div>
  <p class="abs about">About the</p>
  <ul class="abs acronym">
    <li><span class="cap">C</span>ultivating</li>
    <li><span class="cap">L</span>asting</li>
    <li><span class="cap">I</span>nsight,</li>
    <li><span class="cap">M</span>otivation and</li>
    <li><span class="cap">B</span>alance<small>Program</small></li>
  </ul>
  <div class="abs about-copy">
    <p>Chronic stress and burnout are costing organizations millions annually in healthcare costs, employee turnover, and absenteeism.</p>
    <p>The CLIMB Program delivers knowledge, tools, and techniques to empower employees with self-awareness and self-agency, resulting in healthier, more engaged teams.</p>
  </div>
  <p class="abs benefit benefit--1"><span class="benefit__icon"><svg width="16" height="14" viewBox="0 0 16 14" aria-hidden="true"><path d="M8 13 1.5 6.5A3.6 3.6 0 0 1 8 2.2 3.6 3.6 0 0 1 14.5 6.5Z" fill="#5f9a2b"/></svg></span>Increased employee health and engagement</p>
  <p class="abs benefit benefit--2"><span class="benefit__icon"><svg width="16" height="14" viewBox="0 0 16 14" aria-hidden="true"><rect x="1" y="4" width="14" height="9" rx="1.5" fill="#5f9a2b"/><rect x="5" y="1" width="6" height="4" rx="1" fill="none" stroke="#5f9a2b" stroke-width="1.5"/></svg></span>Lower turnover and absenteeism</p>
  <div class="photo" style="left:35px;top:442px;width:230px;height:220px;border-radius:70px 70px 0 0" role="img" aria-label="Black and white photo of two smiling businesswomen with arms crossed"></div>

  <p class="abs framework-title">The <b>CLIMB</b> Program:</p>
  <svg class="abs steps" width="540" height="150" viewBox="0 0 540 150" aria-hidden="true">
    <rect x="10" y="60" width="500" height="10" rx="5" fill="#8fc33a"/>
    <g fill="#eefb8c" font-family="Poppins, sans-serif" font-size="10">
      <g transform="translate(14,0)"><rect x="0" y="52" width="2" height="22"/><path d="M-6 55h12l3 3-3 3h-12z"/><text x="9" y="70">1</text></g>
      <g transform="translate(80,0)"><rect x="0" y="52" width="2" height="22"/><path d="M-6 55h12l3 3-3 3h-12z"/><text x="9" y="70">2</text></g>
      <g transform="translate(150,0)"><rect x="0" y="52" width="2" height="22"/><path d="M-6 55h12l3 3-3 3h-12z"/><text x="9" y="70">3</text></g>
      <g transform="translate(220,0)"><rect x="0" y="52" width="2" height="22"/><path d="M-6 55h12l3 3-3 3h-12z"/><text x="9" y="70">4</text></g>
      <g transform="translate(290,0)"><rect x="0" y="52" width="2" height="22"/><path d="M-6 55h12l3 3-3 3h-12z"/><text x="9" y="70">5</text></g>
      <g transform="translate(355,0)"><rect x="0" y="52" width="2" height="22"/><path d="M-6 55h12l3 3-3 3h-12z"/><text x="9" y="70">6</text></g>
      <g transform="translate(425,0)"><rect x="0" y="52" width="2" height="22"/><path d="M-6 55h12l3 3-3 3h-12z"/><text x="9" y="70">7</text></g>
      <g transform="translate(495,0)"><rect x="0" y="52" width="2" height="22"/><path d="M-6 55h12l3 3-3 3h-12z"/><text x="9" y="70">8</text></g>
    </g>
    <g stroke="#eefb8c" stroke-dasharray="2 2">
      <line x1="15" y1="38" x2="15" y2="52"/><line x1="151" y1="38" x2="151" y2="52"/><line x1="291" y1="38" x2="291" y2="52"/><line x1="426" y1="38" x2="426" y2="52"/>
      <line x1="81" y1="74" x2="81" y2="88"/><line x1="221" y1="74" x2="221" y2="88"/><line x1="356" y1="74" x2="356" y2="88"/><line x1="496" y1="74" x2="496" y2="88"/>
    </g>
  </svg>
  <p class="step-label" style="left:272px;top:48px">The Power<br>of Emotional<br>Regulation</p>
  <p class="step-label" style="left:405px;top:48px">Shifting from<br>Disempowered<br>to Empowered</p>
  <p class="step-label" style="left:545px;top:48px">The Power<br>of What<br>You Believe</p>
  <p class="step-label" style="left:680px;top:48px">The Power<br>of Your<br>Subconscious Mind</p>
  <p class="step-label" style="left:335px;top:146px">Getting in<br>Sync with Your<br>Heart’s Wisdom</p>
  <p class="step-label" style="left:475px;top:146px">Building a<br>Foundation<br>of Coherence</p>
  <p class="step-label" style="left:610px;top:146px">The Power<br>of Your<br>Thoughts</p>
  <p class="step-label" style="left:748px;top:146px">Stepping<br>into Your<br>CLIMB</p>

  <div class="abs panel-goal">
    <p class="goal-lead">Our goal is to empower people to take control of their health and life experiences,</p>
    <p class="goal-head slab">both personally and professionally.</p>
    <p class="tree-title">The CLIMB Program</p>
    <svg class="tree" width="285" height="120" viewBox="0 0 285 120" aria-hidden="true">
      <g stroke="#5f9a2b" stroke-dasharray="3 2" fill="none">
        <path d="M142 5v15M50 20h184M50 20v14M142 20v14M234 20v14"/>
        <path d="M50 76v36M142 76v36M234 76v36"/>
      </g>
    </svg>
    <p class="pillar c1">Learning &amp;<br>Development</p>
    <p class="pillar c2">Personalized<br>Support and<br>Coaching</p>
    <p class="pillar c3">Resources and<br>Engagement<br>Tools</p>
    <p class="tile c1 r1">Online<br>courses</p>
    <p class="tile c1 r2">Monthly topic-<br>specific workshops</p>
    <p class="tile c1 r3">Book study<br>program</p>
    <p class="tile c2 r1">Individual<br>assessments and<br>reporting</p>
    <p class="tile c2 r2">Group coaching</p>
    <p class="tile c2 r3">1:1 coaching</p>
    <p class="tile c3 r1">Promotional<br>Newsletters/emails</p>
    <p class="tile c3 r2">Workplace<br>posters/flyers</p>
    <p class="tile c3 r3">Online Toolkit</p>
  </div>

  <div class="abs invest">
    <p class="invest__lead">Invest in your team.<br>Save on costs.</p>
    <p class="invest__head slab">Gain on<br>Performance.</p>
  </div>
  <div class="abs stat stat--1"><span class="stat__num">30%</span><span class="stat__text">reduction in healthcare costs within 12 months</span></div>
  <div class="abs stat stat--2"><span class="stat__num">25%</span><span class="stat__text">decrease in turnover rates among engaged participants</span></div>
  <div class="abs stat stat--3"><span class="stat__num">40%</span><span class="stat__text">improved productivity among high-stress teams</span></div>

  <div class="abs roi">
    <p>Companies implementing<br>the CLIMB Program<br>report an average</p>
    <p class="roi__value slab">ROI of 3:1</p>
    <p>within the first year.</p>
  </div>
  <div class="abs brand brand--back"><span class="brand__dot"></span>BrindaVale</div>
</section>

</body>
</html>
```